Bref créative
BVSC Stationery
Business Cards/Letterhead
Professional
Bright Valley Skin Clinic
L. Simon Harwick, M.D.
418 Meadowlark Drive
Alcoa, Tennessee 37599
info@brightvalleyskin.example

```html
<!DOCTYPE html>
<html lang="en">
<head>
<meta charset="utf-8">
<title>BVSC Stationery</title>
<link rel="stylesheet" href="https://fonts.googleapis.com/css2?family=Open+Sans:wght@400;600;700&display=swap">
<style>
  :root {
    --backdrop: #e8e6e2;
    --paper: #ffffff;
    --brand-blue: #1f6fb2;
    --deep-blue: #1b4f8a;
    --leaf-green: #8dc63f;
    --dark-green: #5a9a2a;
    --accent-orange: #f7941d;
    --swoosh-blue: #a9cdea;
    --swoosh-yellow: #f6d48a;
    --ink: #4a4a4a;
    --muted: #8a8a8a;
  }
  * { box-sizing: border-box; margin: 0; padding: 0; }
  html, body { width: 1200px; height: 956px; overflow: hidden; }
  body {
    background: var(--backdrop);
    font-family: "Open Sans", Arial, sans-serif;
    color: var(--ink);
    position: relative;
  }
  .sheet {
    position: absolute;
    background: var(--paper);
    box-shadow: 0 2px 6px rgba(0,0,0,0.18);
    overflow: hidden;
  }

  /* Brand name block */
  .brand { display: flex; align-items: center; gap: 8px; }
  .brand-dot { width: 16px; height: 16px; border-radius: 50%; background: var(--accent-orange); flex: none; }
  .brand-name {
    font-weight: 700;
    color: var(--brand-blue);
    line-height: 1.05;
    font-size: 19px;
    letter-spacing: 0.2px;
    max-width: 190px;
  }

  .decor-swoosh {
    position: absolute;
    border-radius: 50%;
    background: radial-gradient(ellipse at 45% 45%, rgba(246,212,138,0.55) 0%, rgba(169,205,234,0.55) 45%, rgba(169,205,234,0) 72%);
  }

  /* Letterhead */
  .letterhead { left: 31px; top: 78px; width: 554px; height: 780px; }
  .letterhead .brand { position: absolute; left: 40px; top: 38px; }
  .letter-date { position: absolute; right: 44px; top: 118px; font-size: 10px; }
  .letter-body {
    position: absolute; left: 40px; top: 146px; width: 470px;
    font-size: 10px; line-height: 1.55;
  }
  .letter-body p { margin-bottom: 11px; }
  .signature {
    width: 70px; height: 26px; margin: 6px 0 4px;
    background: linear-gradient(90deg, rgba(40,40,40,0.35), rgba(40,40,40,0.1));
    border-radius: 12px;
  }
  .letterhead .decor-swoosh { left: 330px; top: 470px; width: 220px; height: 250px; }

  .footer-band { position: absolute; left: 0; right: 0; display: flex; align-items: center; }
  .footer-band .green {
    background: linear-gradient(90deg, var(--dark-green), var(--leaf-green));
    color: #fff; height: 100%; display: flex; align-items: center;
    padding-left: 14px; font-size: 8px; flex: none;
  }
  .footer-band .blue { background: var(--brand-blue); height: 100%; flex: 1; }
  .letterhead .footer-band { bottom: 24px; height: 16px; }
  .letterhead .footer-band .green { width: 380px; }

  /* Envelope */
  .envelope { left: 650px; top: 247px; width: 520px; height: 313px; }
  .envelope .brand { position: absolute; left: 30px; top: 30px; }
  .envelope .decor-swoosh { left: 300px; top: 100px; width: 190px; height: 190px; }
  .envelope .footer-band { bottom: 12px; height: 18px; }
  .envelope .footer-band .green { width: 370px; }

  /* Business card */
  .card { left: 650px; top: 603px; width: 338px; height: 294px; border-radius: 16px; }
  .card .brand { position: absolute; left: 26px; top: 26px; }
  .card .brand-name { font-size: 16px; }
  .card .brand-dot { width: 13px; height: 13px; }
  .card-lower {
    position: absolute; left: 0; right: 0; top: 118px; bottom: 0;
    background: linear-gradient(180deg, #f2f4f6, #dde3ea);
  }
  .contact-panel {
    position: absolute; left: 0; top: 0; bottom: 20px; width: 176px;
    background: linear-gradient(135deg, var(--leaf-green), var(--dark-green));
    padding: 14px 10px 0 14px; color: #fff; font-size: 8px;
  }
  .contact-row { display: flex; align-items: center; gap: 7px; margin-bottom: 9px; line-height: 1.25; }
  .contact-icon {
    width: 15px; height: 15px; border-radius: 50%; background: #fff; flex: none;
    display: flex; align-items: center; justify-content: center;
  }
  .card-holder {
    position: absolute; left: 190px; top: 66px; font-size: 10px;
    color: var(--deep-blue); font-weight: 600;
  }
  .card-base { position: absolute; left: 0; right: 0; bottom: 0; height: 20px; background: var(--brand-blue); }
</style>
</head>
<body>

<section class="sheet letterhead">
  <div class="brand"><span class="brand-dot"></span><span class="brand-name">Bright Valley Skin Clinic</span></div>
  <div class="letter-date">August 3, 2012</div>
  <div class="letter-body">
    <p>Dear Mr. Porter,</p>
    <p>Thank you for choosing our clinic for your recent visit. We are pleased to share the results of your consultation and the next steps in your care plan.</p>
    <p>Our team has reviewed your records and recommends a follow-up appointment within six weeks. Please bring a list of current medications and any questions you may have for the doctor.</p>
    <p>If you need to change your appointment, call our front desk during office hours. We will gladly find a time that works for you and your schedule.</p>
    <p>We look forward to seeing you again soon.</p>
    <p>Yours sincerely,</p>
    <div class="signature" role="img" aria-label="Handwritten signature"></div>
  </div>
  <div class="decor-swoosh" role="img" aria-label="Faint brand swoosh decoration"></div>
  <div class="footer-band">
    <div class="green">418 Meadowlark Drive, Alcoa, Tennessee 37599 &nbsp;·&nbsp; (865) 555-0142</div>
    <div class="blue"></div>
  </div>
</section>

<section class="sheet envelope">
  <div class="brand"><span class="brand-dot"></span><span class="brand-name">Bright Valley Skin Clinic</span></div>
  <div class="decor-swoosh" role="img" aria-label="Faint brand swoosh decoration"></div>
  <div class="footer-band">
    <div class="green">418 Meadowlark Drive, Alcoa, Tennessee 37599 &nbsp;·&nbsp; (865) 555-0142</div>
    <div class="blue"></div>
  </div>
</section>

<section class="sheet card">
  <div class="brand"><span class="brand-dot"></span><span class="brand-name">Bright Valley Skin Clinic</span></div>
  <div class="card-lower">
    <div class="contact-panel">
      <div class="contact-row">
        <span class="contact-icon"><svg width="9" height="9" viewBox="0 0 10 10"><path d="M5 0.5a3.2 3.2 0 0 0-3.2 3.2C1.8 6 5 9.5 5 9.5S8.2 6 8.2 3.7A3.2 3.2 0 0 0 5 0.5zm0 4.4a1.2 1.2 0 1 1 0-2.4 1.2 1.2 0 0 1 0 2.4z" fill="#5a9a2a"/></svg></span>
        <span>418 Meadowlark Drive<br>Alcoa, Tennessee 37599</span>
      </div>
      <div class="contact-row">
        <span class="contact-icon"><svg width="9" height="9" viewBox="0 0 10 10"><path d="M2.2 0.8l1.6 1.9-0.9 1.2c0.6 1.3 1.6 2.3 2.9 2.9l1.2-0.9 1.9 1.6-0.8 1.6C4.5 8.9 1.1 5.5 0.8 1.6z" fill="#5a9a2a"/></svg></span>
        <span>(865) 555-0142</span>
      </div>
      <div class="contact-row">
        <span class="contact-icon"><svg width="9" height="9" viewBox="0 0 10 10"><rect x="2.5" y="0.8" width="5" height="3" fill="#5a9a2a"/><rect x="0.8" y="3.8" width="8.4" height="3.6" rx="0.6" fill="#5a9a2a"/><rect x="2.5" y="6.2" width="5" height="3" fill="#5a9a2a"/></svg></span>
        <span>(865) 555-0143</span>
      </div>
      <div class="contact-row">
        <span class="contact-icon"><svg width="9" height="9" viewBox="0 0 10 10"><rect x="0.8" y="2" width="8.4" height="6" fill="none" stroke="#5a9a2a" stroke-width="1.2"/><path d="M0.8 2l4.2 3.4L9.2 2" fill="none" stroke="#5a9a2a" stroke-width="1.2"/></svg></span>
        <span>info@brightvalleyskin.example</span>
      </div>
    </div>
    <div class="card-holder">L. Simon Harwick, M.D.</div>
    <div class="card-base"></div>
  </div>
</section>

</body>
</html>
```